New Website for QWRB Holdings (Property Leasing Company in New Haven)

Design a fully functioning website for a real estate property leasing company. The company has a few properties in New Haven, CT and would like to provide an option for its tenants to pay their rent online. The company should have the ability to generate unique account log in username and password for its tenants so they can make online payments through ACH the website. (The ACH processing part will be coordinated with the bank).

Please take a look at all the pictures I uploaded of New Haven especially the area around Marlow College, you will find that the general style is Gothic and charming.

Also please make use of the pictures of the two properties I have attached to the description.

Please keep Holdings page, Contact Us Page , About Us Page, and please add a page entitled "Tenants".

On the Holdings page I would like to see on the left hand side an interactive map of new haven (Please see a map attached), split by New Haven's neighbourhoods, and showing my properties as pins of sort on the map (I can send you the addresses of the properties upon request). On the same page on the right side I want to see a drop down menu that includes list of New Haven Neighbourhoods. When a neighbourhood is selected you can see in the space underneath the drop-down menu the properties we have in that neighbourhood in large thumbnail format. Also on the map you can see the pins corresponding to those properties change colour. A user can either click on the pin or on the thumbnails to have view more pictures of the property and some details in text.

The tenants page should prompt a login to access- I like your idea of having the company name in two colours, one for QWRB and another for Holdings.Please let me know if you have any questions along the way

-------------------------------------------------------------------------------
Property Descriptions for Holdings Page
The Larch Lodge,

Neighbourhood: Westville
Name: Silas Brennaway House
Building Style: Queen Anne Style
Address: 418 Pellwin Road, New Haven, CT 06515
Number of Units: 3
Unit Names: Unit 1, Unit 2, Unit 3

Property Description

This Westiville home was built in 1897, historically known as The Silas Brennaway House, it is an example of the Queen Anne style. The large carriage house is still intact and sits in the lovely, expansive back garden! An outstanding architectural feature of the house is the turret, giving the home prominence on Pellwin Road. This well maintained home has renovated kitchens in all units, the first floor has granite and red oak cabinetry. New baths and central air in all apartments. All newer mechanicals for each unit, all natural gas. The entire house has replacement windows. The new back deck overlooks the back garden and carriage house. The front steps and porch have also been rebuilt. Roof has 30 year architectural singles and approximately 15 years old, the chimney has just been lined.

Unit 1 Description:

2 Bedrooms, 6 rooms in total.
Amenities: Dishwasher, Central Air, Gas Heating, Porch

Unit 2 Description:

2 Bedrooms, 5 rooms in total.
Amenities: Dishwasher, Central Air, Gas Heating, Balcony

Unit 3 Description:

2 Bedrooms, 4 rooms in total.
Amenities: Dishwasher, Central Air, Gas Heating

The Fern Lodge:

Neighbourhood: East Rock
Name: 64 Birchmere
Building Style: Victorian
Address: 64 Birchmere Lane, New Haven, CT 06511
Number of Units: 2
Unit Names: Unit 1, and Unit 2

Property Description

East Rock incredibly charming newly renovated 2 family on quiet tree-lined block. Tenants are responsible for all utilities (gas heat, electricity and cable). Small pets are possible with landlord approval. Tenants has use of shared yard, laundry in the basement and on street parking only. Located steps away from gourmet markets & minutes to Downtown New Haven, Marlow & local hospitals. Fascinating backyard. This is a feel good house!

Unit 1 Description:

Area:
1100 soft, 3 Bedrooms, 5 rooms in total.
Amenities: In unit Washer and Dryer, Central Air, Gas Heating, Porch, Backyard

Unit 2 Description:

Area: 2,820 sqft
5 Bedrooms, 8 rooms in total.
Amenities: In unit Washer and Dryer, Dishwasher, Central Air, and Gas Heating

Target Market(s)

1-3 bedroom Renting Market around Marlow College and New Haven Community

Industry/Entity Type

Real Estate

Coding

Coded - Design and coding required

Number of Pages Required

4 page

Font styles to use
Other font styles liked:
• Helvetica

Colors
85cae6
cee9f5
d9d9d9
9d9d9d

Requirements
Must have
• Payment page with login (accounts can only be created by administrator)
• A page showcasing the properties (Professional photos to be uploaded shortly)
• A page for technical support, contact information and so forth
• Home page
Nice to have
• A professional, but stylish design. Not too colourful, something with pastel colours
Should not have
• A lot of colours, any pop-ups,

```html
<!DOCTYPE html>
<html lang="en">
<head>
<meta charset="utf-8">
<title>QWRB Holdings</title>
<link rel="stylesheet" href="https://fonts.googleapis.com/css2?family=Open+Sans:wght@400;600;700&display=swap">
<style>
:root{
  --sky:#85cae6;
  --sky-deep:#3aa3cf;
  --sky-pale:#cee9f5;
  --grey-light:#d9d9d9;
  --grey:#9d9d9d;
  --ink:#333;
  --muted:#777;
  --footer:#2e2f31;
  --footer-deep:#242527;
  --red:#e0302a;
  --white:#fff;
}
*{box-sizing:border-box;margin:0;padding:0}
html,body{width:672px;height:1200px;overflow:hidden}
body{font-family:"Open Sans",Helvetica,Arial,sans-serif;color:var(--ink);background:var(--white);position:relative}
.site-header{height:36px;display:flex;align-items:center;padding:0 27px;position:relative}
.brand{font-size:17px;font-weight:700;color:var(--sky-deep)}
.account{position:absolute;right:27px;top:4px;display:flex;gap:6px}
.account span{font-size:6px;padding:2px 6px;background:var(--grey-light)}
.account span.register{background:var(--sky);color:var(--white)}
.main-nav{position:absolute;right:27px;top:17px;display:flex;gap:2px}
.main-nav a{font-size:7px;color:var(--ink);text-decoration:none;padding:4px 9px}
.main-nav a.active{background:var(--sky);color:var(--white)}
.hero{position:absolute;top:36px;left:0;width:672px;height:234px;background:linear-gradient(180deg,#6f8fb2 0%,#9ab3c9 35%,#4d5a4a 70%,#2f3a2c 100%)}
.search-panel{position:absolute;top:152px;left:94px;width:484px;height:58px;background:rgba(255,255,255,.85);padding:9px 12px}
.search-panel h2{font-size:12.5px;font-weight:700;color:#2c3e50}
.search-panel h2 em{font-style:normal;color:var(--sky-deep)}
.search-row{display:flex;gap:6px;margin-top:7px}
.field{flex:1;height:15px;background:var(--white);border:1px solid var(--grey-light);font-size:6px;color:var(--grey);padding:3px 6px}
.find-btn{height:15px;padding:3px 10px;background:var(--sky-deep);color:var(--white);font-size:6px;font-weight:700}
.section-title{position:absolute;left:0;width:672px;text-align:center}
.section-title h3{font-size:18px;font-weight:600;color:#333}
.section-title p{font-size:6.5px;color:var(--muted);margin-top:2px}
.services{position:absolute;top:354px;left:96px;width:480px;display:flex;justify-content:space-between}
.service{width:120px;text-align:center}
.service svg{display:block;margin:0 auto}
.service h4{font-size:7.5px;font-weight:700;margin-top:6px}
.service p{font-size:6px;color:var(--muted);margin-top:2px;line-height:1.4}
.arrow{position:absolute;top:14px}
.projects{position:absolute;top:538px;left:63px;width:546px;display:grid;grid-template-columns:repeat(3,176px);gap:9px 9px}
.card{height:124px;border:1px solid var(--grey-light);padding:6px;background:var(--white)}
.card h5{font-size:7.5px;font-weight:700;margin-bottom:5px}
.card-body{display:flex;gap:5px}
.card-photo{width:84px;height:58px;background:linear-gradient(180deg,#7fa9cf,#b8c9b0 55%,#5f7050)}
.card-info{flex:1}
.card-tag{background:var(--sky-deep);color:var(--white);font-size:5.5px;padding:2px 3px}
.card-info p{font-size:5.5px;color:var(--muted);line-height:1.4;margin-top:3px}
.card-info a{font-size:5.5px;color:var(--sky-deep);display:block;margin-top:2px}
.card-stats{display:flex;justify-content:space-between;border-top:1px solid var(--grey-light);margin-top:7px;padding-top:6px;font-size:5.5px;color:var(--muted)}
.ach-band{position:absolute;top:809px;left:0;width:672px;height:46px;background:var(--sky-deep);display:flex;align-items:center;justify-content:center;gap:26px}
.ach-band p{color:var(--white);font-size:11px}
.pay-btn{background:var(--red);color:var(--white);font-size:7px;font-weight:700;padding:5px 12px;border-radius:10px}
.testimonials{position:absolute;top:924px;left:60px;width:552px;display:flex;justify-content:space-between}
.testimonial{width:250px;display:flex;gap:12px;align-items:flex-start}
.avatar{width:36px;height:36px;border-radius:50%;flex:none;background:linear-gradient(180deg,#c9a98c,#8a6a52)}
.testimonial p{font-size:6px;color:var(--muted);line-height:1.5}
.testimonial strong{display:block;font-size:7px;margin-top:6px;color:var(--ink)}
.pager{position:absolute;top:980px;left:322px;display:flex;gap:8px}
.site-footer{position:absolute;top:1024px;left:0;width:672px;height:176px;background:var(--footer);color:#ccc}
.footer-cols{display:flex;padding:12px 27px 0;gap:20px}
.footer-col{width:140px}
.footer-col h6{font-size:8px;font-weight:600;color:var(--white);margin-bottom:8px;padding-bottom:4px;border-bottom:1px solid #444}
.contact-line{display:flex;gap:6px;align-items:center;font-size:5.5px;margin-bottom:7px;line-height:1.4}
.contact-line i{width:14px;height:14px;border:1px solid #777;border-radius:50%;flex:none;display:flex;align-items:center;justify-content:center}
.info-list{list-style:none;font-size:6px}
.info-list li{margin-bottom:5px}
.info-list li::before{content:"›";color:var(--sky);margin-right:5px}
.thumbs{display:grid;grid-template-columns:repeat(3,38px);gap:4px}
.thumbs span{height:30px;background:linear-gradient(180deg,#7a9cbc,#6a7d5b)}
.input{height:11px;background:#3b3c3e;border:1px solid #4a4b4d;font-size:5.5px;padding:2px 4px;margin-bottom:4px;color:#999}
.input.tall{height:22px}
.submit{display:inline-block;background:var(--sky-deep);color:var(--white);font-size:6px;padding:2px 8px}
.footer-bar{position:absolute;bottom:0;left:0;width:672px;height:36px;background:var(--footer-deep);display:flex;align-items:center;justify-content:space-between;padding:0 27px}
.footer-bar p{font-size:6px;color:#aaa}
.socials{display:flex;gap:5px}
.socials span{width:14px;height:14px;border-radius:50%;background:#555}
</style>
</head>
<body>
<header class="site-header">
  <div class="brand">QWRB Holdings</div>
  <div class="account"><span>Login</span><span class="register">Register</span></div>
  <nav class="main-nav">
    <a class="active" href="#">Home</a><a href="#">About Us</a><a href="#">Listing</a><a href="#">Property</a><a href="#">Rentals</a><a href="#">Contact Us</a>
  </nav>
</header>

<section class="hero" role="img" aria-label="Photo of a large two-storey family house with trees under a blue sky"></section>
<form class="search-panel">
  <h2>Rent To Own properties Available Where You Live Absolutely <em>100% FREE</em></h2>
  <div class="search-row">
    <div class="field">First Name</div><div class="field">Your Email</div><div class="field">Target City</div>
    <div class="find-btn">FIND MY LISTING</div>
  </div>
</form>

<div class="section-title" style="top:300px"><h3>Our Service</h3><p>Lorem ipsum dolor sit amet, consectetur adipiscing elit. Curabitur iaculis lacus in dictum tempor nisi.</p></div>
<div class="services">
  <div class="service">
    <svg width="30" height="30" viewBox="0 0 30 30"><path d="M3 15 15 4l12 11" fill="none" stroke="#c0392b" stroke-width="3"/><rect x="8" y="14" width="14" height="12" fill="#666"/></svg>
    <h4>Search Details</h4><p>Lorem ipsum dolor sit amet, consecte tur adipiscing elit.</p>
  </div>
  <div class="service">
    <svg width="30" height="30" viewBox="0 0 30 30"><path d="M3 15 15 4l12 11" fill="none" stroke="#27ae60" stroke-width="3"/><rect x="8" y="14" width="14" height="12" fill="#666"/><path d="M11 20l3 3 6-6" fill="none" stroke="#fff" stroke-width="2"/></svg>
    <h4>Confirm Details</h4><p>Lorem ipsum dolor sit amet, consecte tur adipiscing elit.</p>
  </div>
  <div class="service">
    <svg width="30" height="30" viewBox="0 0 30 30"><rect x="4" y="5" width="22" height="20" rx="2" fill="#2f6e5a"/><path d="M8 11h14M8 15h14M8 19h10" stroke="#fff" stroke-width="1.5"/></svg>
    <h4>Done! View Listing</h4><p>Lorem ipsum dolor sit amet, consecte tur adipiscing elit.</p>
  </div>
  <svg class="arrow" style="left:125px" width="30" height="10" viewBox="0 0 30 10"><path d="M1 7q14-8 26 0m-4-3 4 3-5 1" fill="none" stroke="#999"/></svg>
  <svg class="arrow" style="left:305px" width="30" height="10" viewBox="0 0 30 10"><path d="M1 7q14-8 26 0m-4-3 4 3-5 1" fill="none" stroke="#999"/></svg>
</div>

<div class="section-title" style="top:472px"><h3>Our Project</h3><p>Lorem ipsum dolor sit amet, consectetur adipiscing elit. Curabitur iaculis lacus in dictum tempor.</p></div>
<div class="projects">
  <article class="card"><h5>4BR/3BA Single Family House</h5><div class="card-body"><div class="card-photo" role="img" aria-label="Photo of a single family house"></div><div class="card-info"><div class="card-tag">Lorem ipsum dolor</div><p>Lorem ipsum dolor sit amet, consecte tur adipiscing elit.</p><a>Read More</a></div></div><div class="card-stats"><span>3 Bed</span><span>2 Bath</span><span>1100 sqft</span></div></article>
  <article class="card"><h5>4BR/3BA Single Family House</h5><div class="card-body"><div class="card-photo" role="img" aria-label="Photo of a single family house"></div><div class="card-info"><div class="card-tag">Lorem ipsum dolor</div><p>Lorem ipsum dolor sit amet, consecte tur adipiscing elit.</p><a>Read More</a></div></div><div class="card-stats"><span>3 Bed</span><span>2 Bath</span><span>1100 sqft</span></div></article>
  <article class="card"><h5>4BR/3BA Single Family House</h5><div class="card-body"><div class="card-photo" role="img" aria-label="Photo of a single family house"></div><div class="card-info"><div class="card-tag">Lorem ipsum dolor</div><p>Lorem ipsum dolor sit amet, consecte tur adipiscing elit.</p><a>Read More</a></div></div><div class="card-stats"><span>3 Bed</span><span>2 Bath</span><span>1100 sqft</span></div></article>
  <article class="card"><h5>4BR/3BA Single Family House</h5><div class="card-body"><div class="card-photo" role="img" aria-label="Photo of a single family house"></div><div class="card-info"><div class="card-tag">Lorem ipsum dolor</div><p>Lorem ipsum dolor sit amet, consecte tur adipiscing elit.</p><a>Read More</a></div></div><div class="card-stats"><span>3 Bed</span><span>2 Bath</span><span>1100 sqft</span></div></article>
  <article class="card"><h5>4BR/3BA Single Family House</h5><div class="card-body"><div class="card-photo" role="img" aria-label="Photo of a single family house"></div><div class="card-info"><div class="card-tag">Lorem ipsum dolor</div><p>Lorem ipsum dolor sit amet, consecte tur adipiscing elit.</p><a>Read More</a></div></div><div class="card-stats"><span>3 Bed</span><span>2 Bath</span><span>1100 sqft</span></div></article>
  <article class="card"><h5>4BR/3BA Single Family House</h5><div class="card-body"><div class="card-photo" role="img" aria-label="Photo of a single family house"></div><div class="card-info"><div class="card-tag">Lorem ipsum dolor</div><p>Lorem ipsum dolor sit amet, consecte tur adipiscing elit.</p><a>Read More</a></div></div><div class="card-stats"><span>3 Bed</span><span>2 Bath</span><span>1100 sqft</span></div></article>
</div>

<section class="ach-band"><p>ACH processing make online payments through their Rent online</p><span class="pay-btn">PAY ONLINE NOW</span></section>

<div class="section-title" style="top:870px"><h3>Testimonials</h3><p style="font-size:9px;font-style:italic">Lorem ipsum dolor sit amet, consectetur adipiscing elit</p></div>
<div class="testimonials">
  <div class="testimonial"><div class="avatar" role="img" aria-label="Portrait photo of the tenant"></div><div><p>Lorem ipsum dolor sit amet, consectetur adipiscing elit. Praesent iaculis lobortis aliquam. Nam et rutrum ante. Nulla eget nisl.</p><strong>Nora Halvey</strong></div></div>
  <div class="testimonial"><div class="avatar" role="img" aria-label="Portrait photo of the tenant"></div><div><p>Lorem ipsum dolor sit amet, consectetur adipiscing elit. Praesent iaculis lobortis aliquam. Nam et rutrum ante. Nulla eget nisl.</p><strong>Nora Halvey</strong></div></div>
</div>
<div class="pager">
  <svg width="10" height="12" viewBox="0 0 10 12"><path d="M8 1 2 6l6 5" fill="none" stroke="#999" stroke-width="2"/></svg>
  <svg width="10" height="12" viewBox="0 0 10 12"><path d="M2 1l6 5-6 5" fill="none" stroke="#999" stroke-width="2"/></svg>
</div>

<footer class="site-footer">
  <div class="footer-cols">
    <div class="footer-col"><h6>Contact Us</h6>
      <div class="contact-line"><i><svg width="6" height="8" viewBox="0 0 6 8"><path d="M3 8 0.5 3.5A2.5 2.5 0 1 1 5.5 3.5Z" fill="#aaa"/></svg></i><span>Lorem ipsum dolor sit amet, consectetur elit</span></div>
      <div class="contact-line"><i><svg width="7" height="7" viewBox="0 0 7 7"><path d="M1 0h2l1 2-1 1a4 4 0 0 0 2 2l1-1 1 1v2C3 7 0 4 0 1Z" fill="#aaa"/></svg></i><span>(000) 555-0142</span></div>
      <div class="contact-line"><i><svg width="7" height="5" viewBox="0 0 7 5"><rect width="7" height="5" fill="none" stroke="#aaa"/><path d="M0 0l3.5 3L7 0" fill="none" stroke="#aaa"/></svg></i><span>hello@qwrbholdings.com</span></div>
    </div>
    <div class="footer-col"><h6>Information</h6>
      <ul class="info-list"><li>Home</li><li>Legal notice</li><li>Terms and conditions</li><li>Secure payment</li><li>Site map</li></ul>
    </div>
    <div class="footer-col"><h6>Properties</h6>
      <div class="thumbs" role="img" aria-label="Small photos of the company's rental houses"><span></span><span></span><span></span><span></span><span></span><span></span></div>
    </div>
    <div class="footer-col"><h6>Quick Message</h6>
      <div class="input">Name</div><div class="input">Email</div><div class="input tall">Message</div><span class="submit">Submit</span>
    </div>
  </div>
  <div class="footer-bar"><p>©2023 QWRB Holdings All rights reserved.</p><div class="socials"><span></span><span></span><span></span><span></span><span></span><span></span></div></div>
</footer>
</body>
</html>
```